Funken-und-Fragen Flyer
Zielgruppe
Eltern, die ihre Kinder in ihrer Entwicklung fördern möchten.
Aufgabenstellung
Wir organisieren eine Messe mit dem Thema "Funken und Fragen". Bei der Messe geht es nicht um das Lernen über Bücher (alleine) oder das Schulische, sondern die Messe soll für Eltern sein, die ihre Kinder fördern möchten durch die Behebung von Lernblockaden, Förderung der Konzentration, Kreativität, spielerisches Lernen etc. Es geht um Kinder ab ca. 4 Jahren.
Als Aussteller werden verschiedene Themen angesprochen: Kinesiologie, Logopädie, Privatschulen mit speziellem Angenbot, Schachunterricht, spielerisches Lernangebot, Kindermalen etc. , alles was darauf zielt, Kreativität und Lernen bei Kindern zu fördern.
Wir brauchen daher einen Flyer, der die Eltern anspricht. Die Messe findet am Sonntag, 9.11.2012 statt. Beginn 11 Uhr, Ende 18.00 Uhr. Ort: Seeforumhalle - Lindensaal, Wendelgasse 7, 8047 Zürich.
Das Logo wird attached. Das Format ist frei wählbar.

```html
<!DOCTYPE html>
<html lang="de">
<head>
<meta charset="utf-8">
<title>Funken und Fragen – Messe Flyer</title>
<link rel="stylesheet" href="https://fonts.googleapis.com/css2?family=Bebas+Neue&family=Ubuntu:wght@400;500&family=Gochi+Hand&display=swap">
<style>
  :root {
    --blue: #0a9fdc;
    --purple: #8f0f7a;
    --orange: #f0900a;
    --teal: #098a8f;
    --white: #ffffff;
    --text-grey: #555555;
    --backdrop: #e6e6e6;
    --photo-light: #f3ebe0;
    --photo-warm: #d9b68e;
    --photo-floor: #c99a6a;
  }
  * { margin: 0; padding: 0; box-sizing: border-box; }
  html, body {
    width: 1200px; height: 1200px; overflow: hidden;
    background: var(--backdrop);
  }
  .flyer {
    position: absolute; left: 195px; top: 30px;
    width: 810px; height: 1140px;
    background: var(--white);
    display: flex; flex-direction: column;
    font-family: "Ubuntu", sans-serif;
    box-shadow: 0 4px 14px rgba(0,0,0,0.25);
    overflow: hidden;
  }
  .flyer-head {
    height: 219px; position: relative; flex: none;
  }
  .benefits {
    position: absolute; left: 0; top: 22px;
    display: flex; flex-direction: column; gap: 12px;
    list-style: none;
  }
  .benefit {
    width: 378px; height: 50px;
    color: var(--white); font-size: 24px; font-weight: 500;
    padding-left: 18px; line-height: 50px; letter-spacing: 0.5px;
    white-space: nowrap;
    box-shadow: 3px 3px 4px rgba(0,0,0,0.3);
  }
  .benefit--blue { background: var(--blue); }
  .benefit--purple { background: var(--purple); }
  .benefit--orange { background: var(--orange); }
  .brand {
    position: absolute; right: 30px; top: 150px;
    text-align: right;
  }
  .brand-row { display: flex; align-items: center; gap: 12px; justify-content: flex-end; }
  .brand-dot { width: 22px; height: 22px; border-radius: 50%; background: var(--teal); }
  .brand-name { color: var(--teal); font-size: 34px; font-weight: 400; white-space: nowrap; }
  .brand-url { color: var(--text-grey); font-size: 13px; margin-top: 4px; }
  .title-band {
    height: 106px; background: var(--teal); flex: none;
    display: flex; align-items: center; justify-content: center;
    overflow: hidden;
  }
  .title {
    font-family: "Bebas Neue", sans-serif; color: var(--white);
    font-size: 74px; font-weight: 400; letter-spacing: 1px;
    line-height: 1; padding-top: 6px; white-space: nowrap;
  }
  .date-band {
    height: 73px; background: var(--purple); margin-top: 3px; flex: none;
    display: flex; align-items: center; justify-content: center;
    color: var(--white); font-size: 28px; font-weight: 500; white-space: nowrap;
  }
  .photo {
    height: 471px; flex: none;
    background: linear-gradient(180deg, var(--photo-light) 0%, #ead9c2 55%, var(--photo-warm) 80%, var(--photo-floor) 100%);
  }
  .venue-band {
    height: 106px; background: var(--purple); flex: none;
    display: flex; flex-direction: column; align-items: center; justify-content: center;
    color: var(--white); font-size: 27px; font-weight: 500; line-height: 1.25;
    border-top: 3px solid var(--white);
  }
  .slogan-band {
    height: 110px; background: var(--teal); margin-top: 3px; flex: none;
    display: flex; align-items: center; justify-content: center; text-align: center;
    color: var(--white); font-family: "Gochi Hand", cursive;
    font-size: 34px; line-height: 1.05; padding: 0 30px;
  }
  .organizer {
    flex: 1; display: flex; align-items: center; justify-content: center;
    color: var(--purple); font-size: 20px; font-weight: 500; white-space: nowrap;
  }
</style>
</head>
<body>
  <main class="flyer">
    <header class="flyer-head">
      <ul class="benefits">
        <li class="benefit benefit--blue">- Begabungen erkennen</li>
        <li class="benefit benefit--purple">- Konzentration fördern</li>
        <li class="benefit benefit--orange">- Lernen entfalten</li>
      </ul>
      <div class="brand">
        <div class="brand-row">
          <span class="brand-dot"></span>
          <span class="brand-name">Funken und Fragen</span>
        </div>
        <div class="brand-url">www.funkenundfragen.ch</div>
      </div>
    </header>
    <section class="title-band">
      <h1 class="title">Messe "Funken und Fragen"</h1>
    </section>
    <section class="date-band">Sonntag 09.11.2012 | 11.00 - 18.00 Uhr</section>
    <div class="photo" role="img" aria-label="Foto: eine Betreuerin mit zwei Kindern vor einer Magnettafel mit bunten Zahlen in einem hellen Spielzimmer"></div>
    <section class="venue-band">
      <p>Seeforumhalle - Lindensaal</p>
      <p>Wendelgasse 7, 8047 Zürich</p>
    </section>
    <section class="slogan-band">
      <p>Damit Kinder ihre aktuellen und zukünftigen<br>Herausforderungen spielend meistern!</p>
    </section>
    <footer class="organizer">Veranstalter: Funkenundfragen GmbH, Am Bühlweg 12, 8805 Richterswil</footer>
  </main>
</body>
</html>
```